Business Card Design Project For Moving Company

Hello,

We need the business card to be 2 sided and we were thinking to use the logo on the front of the card (see file 1 attached) and the text "logo" (see file 2 attached) in the back of the card. We're looking for a powerful design that will help us build our brand, as our company is new.
We are a full service moving company (no storage) located in San Diego, CA, USA. The design should communicate to our potential customers that we have the highest level of service, customer satisfaction is our number one goal, our team is professional and efficient.

Thank you,

Dorn
Updates

Project Deadline Extended
Reason: We would like to have more time to provide feedback for the designs already submitted. Thank you, Dorn

Industry/Entity Type

Moving Company

Requirements
Must have
• Front of the card must have the following text and logo:
Haulbright, Inc
Residential And Commercial
Local And Long Distance
Address: 7312 Quillmont Rd, #146,
San Diego, CA, 92784
P: 855-372-LIFT (5438)
F: 858-529-4407
info@haul-bright.com
www.haul-bright.com

Back of the card must have the following text and text "logo" (file 2 attached):

The best compliment we can ever receive is a referral from our clients.

```html
<!DOCTYPE html>
<html lang="en">
<head>
<meta charset="utf-8">
<title>Haulbright, Inc — Business Card</title>
<link rel="stylesheet" href="https://fonts.googleapis.com/css2?family=Open+Sans:ital,wght@0,700;1,400&family=Roboto+Condensed:ital,wght@0,700;1,400&display=swap">
<style>
  :root {
    --paper: #ffffff;
    --ink: #111111;
    --brand-red: #e0131f;
    --red-top: #ec1423;
    --red-bottom: #a90912;
    --band-dark: #151515;
    --frame: #3a3a3a;
    --on-red: #ffffff;
  }
  html, body {
    margin: 0;
    padding: 0;
    width: 1200px;
    height: 720px;
    overflow: hidden;
    background: var(--paper);
  }
  .card {
    position: relative;
    width: 1200px;
    height: 720px;
    background: var(--paper);
    overflow: hidden;
    box-shadow: inset 0 0 0 3px var(--frame), inset 0 0 10px 4px rgba(0,0,0,0.45);
  }
  .swoosh {
    position: absolute;
    inset: 0;
    width: 1200px;
    height: 720px;
  }
  .wordmark {
    position: absolute;
    left: 44px;
    top: 182px;
    margin: 0;
    font-family: "Roboto Condensed", "Arial Narrow", sans-serif;
    font-weight: 700;
    font-size: 128px;
    line-height: 1;
    letter-spacing: -1.5px;
    color: var(--brand-red);
    text-transform: uppercase;
    white-space: nowrap;
  }
  .divider {
    position: absolute;
    left: 720px;
    top: 129px;
    width: 3px;
    height: 253px;
    background: var(--ink);
  }
  .services {
    position: absolute;
    left: 740px;
    top: 158px;
    margin: 0;
    padding: 0;
    list-style: none;
    font-family: "Roboto Condensed", "Arial Narrow", sans-serif;
    font-style: italic;
    font-weight: 400;
    font-size: 44px;
    line-height: 65px;
    letter-spacing: -1.2px;
    color: var(--ink);
    white-space: nowrap;
  }
  .services li:nth-child(3) { margin-left: -6px; }
  .contact {
    position: absolute;
    right: 8px;
    top: 490px;
    margin: 0;
    text-align: right;
    font-family: "Open Sans", Arial, sans-serif;
    font-style: italic;
    font-size: 24px;
    line-height: 37.5px;
    color: var(--on-red);
    white-space: nowrap;
  }
  .contact .label {
    font-style: normal;
    font-weight: 700;
    font-size: 25px;
  }
  .web-line {
    position: absolute;
    right: 12px;
    top: 682px;
    margin: 0;
    font-family: "Open Sans", Arial, sans-serif;
    font-weight: 700;
    font-size: 21px;
    line-height: 1;
    color: var(--on-red);
    white-space: nowrap;
  }
  .web-line .sep { margin: 0 12px; }
</style>
</head>
<body>
  <div class="card">
    <svg class="swoosh" viewBox="0 0 1200 720" aria-hidden="true">
      <defs>
        <linearGradient id="redFill" x1="0" y1="0" x2="0" y2="1">
          <stop offset="0" stop-color="var(--red-top)"/>
          <stop offset="1" stop-color="var(--red-bottom)"/>
        </linearGradient>
      </defs>
      <path fill="var(--band-dark)" d="M0,604 C300,590 590,548 800,474 C950,424 1080,416 1200,418 L1200,720 L0,720 Z"/>
      <path fill="url(#redFill)" d="M0,630 C310,612 610,566 820,494 C960,446 1085,428 1200,430 L1200,720 L0,720 Z"/>
    </svg>

    <p class="wordmark">Haulbright</p>

    <div class="divider"></div>

    <ul class="services">
      <li>Haulbright, Inc</li>
      <li>Residential And Commercial</li>
      <li>Local And Long Distance</li>
    </ul>

    <p class="contact">
      <span class="label">Address</span>: 7312 Quillmont Rd, #146,<br>
      San Diego, CA, 92784<br>
      P: 855-372-LIFT (5438)<br>
      F: 858-529-4407
    </p>

    <p class="web-line">URL: www.haul-bright.com<span class="sep">|</span>E-Mail: info@haul-bright.com</p>
  </div>
</body>
</html>
```